Business Card Design for Kidvale (Hires out childrens play areas)

Looking to have a business card designed for a company we just bought. The company rents out childrens play areas.

I have uploaded a couple of examples of the kind of business card style I like. Here are two more examples:

https://quorvastudio.nz/project/bright-romp-branding/
https://imgvaultcdn.com/design_img/8841052/302917/302917_5518203_8841052_b73e19a2_image.jpg

I think a white card will be best due to all the colours in the logo.

Size we require: 3.75" x 2.25" (horizontally orientated) with a 0.125" bleed

Uploaded is two versions of our logo.

Details for the card:
1. My name: Liam Verster
2. Title: Managing Director
3. Phone no: 021 563 417
4. Email: liam@kidvale.co.nz
5. URL: www.kidvale.co.nz
6. Address:
PO Box 318625
Fernlea, Auckland

Let me know if you need anything else.

Target Market(s)

Hospitals, doctors surgeries, bed shops, etc.

Contact Information for Business Card

Details for the card:
1. My name: Liam Verster
3. Phone no: 021 563 417
5. URL: www.kidvale.co.nz
6. Address:
PO Box 318625
Fernlea, Auckland

Requirements
Should not have
• Not too busy.

```html
<!DOCTYPE html>
<html lang="en">
<head>
<meta charset="utf-8">
<title>Kidvale Business Card – Back and Front</title>
<link href="https://fonts.googleapis.com/css2?family=PT+Sans:wght@400;700&display=swap" rel="stylesheet">
<style>
  :root {
    --backdrop: #2b2b2b;
    --card-black: #000000;
    --teal: #0e959d;
    --edge-blue: #1a5cab;
    --text-white: #f4f4f4;
    --accent-orange: #f28a1e;
  }
  * { margin: 0; padding: 0; box-sizing: border-box; }
  html, body {
    width: 1200px; height: 923px; overflow: hidden;
    background: var(--backdrop);
    font-family: "PT Sans", Arial, sans-serif;
  }
  .card {
    position: absolute; left: 270px;
    width: 660px; height: 396px;
    background: var(--card-black);
    overflow: hidden;
  }
  .card-back { top: 45px; }
  .card-front { top: 482px; }
  .card-bands { position: absolute; inset: 0; width: 100%; height: 100%; }

  .brand { position: absolute; display: flex; align-items: center; gap: 12px; }
  .brand-dot { border-radius: 50%; background: var(--accent-orange); flex: none; }
  .brand-name { font-weight: 700; line-height: 1; color: var(--text-white); letter-spacing: 1px; }

  .card-back .brand { left: 0; right: 0; top: 150px; justify-content: center; gap: 16px; }
  .card-back .brand-dot { width: 38px; height: 38px; }
  .card-back .brand-name { font-size: 72px; }

  .card-front .brand { left: 240px; top: 96px; }
  .card-front .brand-dot { width: 30px; height: 30px; }
  .card-front .brand-name { font-size: 56px; }

  .person { position: absolute; left: 96px; top: 252px; }
  .person-name { font-size: 33px; font-weight: 400; color: var(--teal); line-height: 1.05; }
  .person-title { font-size: 18px; color: var(--text-white); margin-left: 24px; line-height: 1.25; }

  .divider {
    position: absolute; left: 318px; top: 198px;
    width: 1.5px; height: 116px; background: var(--text-white); opacity: .8;
  }
  .contact-list { position: absolute; left: 342px; top: 196px; list-style: none; }
  .contact-item {
    display: flex; align-items: flex-start; gap: 10px;
    font-size: 16px; color: var(--text-white); line-height: 23px;
  }
  .contact-icon {
    flex: none; width: 15px; height: 15px; margin-top: 4px;
    background: var(--teal); border-radius: 2px;
    display: flex; align-items: center; justify-content: center;
  }
  .contact-icon svg { width: 11px; height: 11px; }
</style>
</head>
<body>
  <div class="card card-back">
    <div class="brand">
      <span class="brand-dot"></span>
      <span class="brand-name">Kidvale</span>
    </div>
  </div>

  <div class="card card-front">
    <svg class="card-bands" viewBox="0 0 1000 600" preserveAspectRatio="none" aria-hidden="true">
      <path d="M0 0 H1000 V92 C720 60 360 30 0 44 Z" fill="var(--edge-blue)"/>
      <path d="M0 0 H1000 V80 C720 48 360 20 0 32 Z" fill="var(--teal)"/>
      <path d="M0 510 C340 548 690 560 1000 530 V600 H0 Z" fill="var(--edge-blue)"/>
      <path d="M0 522 C340 560 690 572 1000 542 V600 H0 Z" fill="var(--teal)"/>
    </svg>

    <div class="brand">
      <span class="brand-dot"></span>
      <span class="brand-name">Kidvale</span>
    </div>

    <div class="person">
      <div class="person-name">Liam Verster</div>
      <div class="person-title">Managing Director</div>
    </div>

    <div class="divider"></div>

    <ul class="contact-list">
      <li class="contact-item">
        <span class="contact-icon"><svg viewBox="0 0 16 16"><path d="M4 2 L6.5 5 L5 6.5 C6 8.5 7.5 10 9.5 11 L11 9.5 L14 12 L12.5 14 C7 13.5 2.5 9 2 3.5 Z" fill="#000"/></svg></span>
        <span>021 563 417</span>
      </li>
      <li class="contact-item">
        <span class="contact-icon"><svg viewBox="0 0 16 16"><rect x="2" y="4" width="12" height="8" fill="none" stroke="#000" stroke-width="1.6"/><path d="M2 4 L8 9 L14 4" fill="none" stroke="#000" stroke-width="1.6"/></svg></span>
        <span>liam@kidvale.co.nz</span>
      </li>
      <li class="contact-item">
        <span class="contact-icon"><svg viewBox="0 0 16 16"><circle cx="8" cy="8" r="5.5" fill="none" stroke="#000" stroke-width="1.5"/><path d="M2.5 8 H13.5 M8 2.5 C5.5 5 5.5 11 8 13.5 M8 2.5 C10.5 5 10.5 11 8 13.5" fill="none" stroke="#000" stroke-width="1.2"/></svg></span>
        <span>www.kidvale.co.nz</span>
      </li>
      <li class="contact-item">
        <span class="contact-icon"><svg viewBox="0 0 16 16"><path d="M8 14 C4.5 9.5 3.5 8 3.5 6 A4.5 4.5 0 0 1 12.5 6 C12.5 8 11.5 9.5 8 14 Z" fill="#000"/><circle cx="8" cy="6" r="1.7" fill="var(--teal)"/></svg></span>
        <span>PO Box 318625<br>Fernlea, Auckland</span>
      </li>
    </ul>
  </div>
</body>
</html>
```